Letterhead for 3 attorney Workers' Comp law firm

We are a 3 attorney law office. We specialize in Workers' Compensation. Our office represents workers who are injured on the job, and the estates of workers who are killed one the job.
When we started our office, we created our own letterhead & have been using it for years. We've just recently hired the 3rd attorney, and were going to just add his name to the letterhead, but have decided we wanted to get a professionally designed letterhead and business cards at this point.
We want something that looks clean and professional. It must look good in black and white because we often make multiple copies of our documents. We're hoping for a design that resonates confidence, reliability and experience.
The design must include the firm name: Thornbury & Calder, PLLC. We would like the PLLC to be small compared to the Thornbury & Calder graphic. We also want to incorporate the attorney names: Ivar Thornbury, Delia Calder, and Glen Rutledge. Our current letterhead has our contact info in the footer at the bottom of the page. We like that design, but are open to the idea of having it at the top. We'll leave that at the discretion of the designer. Our contact info is as follows: 482 S. Harrow Avenue, Suite 310 Bellingham, WA 98417 Phone: 360-555-2917, Fax: 360-555-4068, and our website: www.thornburycalder.example
Target Market(s)
Clients, courts, other legal offices, doctors offices. These are the people who see our letterhead most frequently. It's not so much for marketing purposes, mainly so that we have a professional image when sending out documents.
Industry/Entity Type
Law Firm
Contact Information for Business Card
On the back of the business card: it can be designed, or be a template for filling in appointment reminder information (i.e. date, time, etc)
Colors
Designer to choose colors to be used in the design.
Requirements
Must have
- Must have our firm name at the top.
- Must include the attorney names.
- Must have all of our contact information (can be at top or bottom - whatever looks best with the design)
Nice to have
- A strong, confident design
Should not have
- We don't want the design to be playful, cartoony or busy.

```html
<!DOCTYPE html>
<html lang="en">
<head>
<meta charset="utf-8">
<title>Thornbury &amp; Calder, PLLC — Letterhead</title>
<link rel="stylesheet" href="https://fonts.googleapis.com/css2?family=Cinzel:wght@400;500&family=Lato:wght@300;400&display=swap">
<style>
  :root {
    --backdrop: #e6e6e6;
    --paper: #ffffff;
    --ink: #1f1f1f;
    --ink-soft: #3a3a3a;
    --rule: #2b2b2b;
    --band: #3d3d3d;
  }
  * { box-sizing: border-box; margin: 0; padding: 0; }
  html, body {
    width: 1200px; height: 1200px; overflow: hidden;
    background: var(--backdrop);
  }
  .canvas {
    width: 1200px; height: 1200px;
    display: flex; align-items: center; justify-content: center;
  }
  .letterhead {
    position: relative;
    width: 792px; height: 1120px;
    background: var(--paper);
    box-shadow: 0 2px 10px rgba(0,0,0,0.08);
    color: var(--ink);
    font-family: "Lato", sans-serif;
  }
  .firm-name {
    position: absolute; left: 60px; top: 92px;
    font-family: "Cinzel", serif;
    font-weight: 400;
    font-size: 26px;
    letter-spacing: 1.5px;
    color: var(--ink);
  }
  .firm-name .suffix { font-size: 19px; }
  .attorney-list {
    position: absolute; right: 62px; top: 52px;
    border-left: 1.5px solid var(--rule);
    padding: 2px 0 2px 12px;
    font-size: 10px; line-height: 1.3;
    color: var(--ink-soft);
  }
  .attorney-list .label {
    font-family: "Cinzel", serif;
    font-size: 11px; letter-spacing: 0.5px;
    color: var(--ink);
  }
  .letter-body {
    position: absolute; left: 150px; right: 70px; top: 262px;
    font-size: 15px; line-height: 1.52; font-weight: 300;
    color: var(--ink-soft);
  }
  .salutation { font-weight: 400; color: var(--ink); margin-bottom: 22px; }
  .letter-body p + p { margin-top: 30px; }
  .sign-off { position: absolute; left: 390px; top: 740px; }
  .signature { width: 70px; height: 46px; background: linear-gradient(135deg, #f2f2f2, #e3e3e3); border-radius: 3px; }
  .signer-name { font-size: 19px; font-weight: 400; margin-top: 10px; color: var(--ink); }
  .signer-title { font-size: 14px; font-weight: 300; color: var(--ink-soft); margin-top: 4px; }
  .contact-footer {
    position: absolute; right: 60px; bottom: 46px;
    text-align: left;
    font-size: 12.5px; line-height: 1.6; color: var(--ink);
  }
  .contact-footer .line { display: flex; align-items: center; gap: 6px; }
  .contact-footer svg { width: 12px; height: 12px; flex: none; }
  .bottom-band {
    position: absolute; left: 0; right: 0; bottom: 0; height: 9px;
    background: var(--band);
  }
</style>
</head>
<body>
<main class="canvas">
  <article class="letterhead">
    <h1 class="firm-name">Thornbury &amp; Calder, <span class="suffix">PLLC</span></h1>

    <div class="attorney-list">
      <div class="label">ATTORNEY</div>
      <div>Ivar Thornbury</div>
      <div>Delia Calder</div>
      <div>Glen Rutledge</div>
    </div>

    <section class="letter-body">
      <div class="salutation">Dear Mr. Ellison,</div>
      <p>Lorem ipsum dolor sit amet, consectetur adipiscing elit. Donec orci purus, luctus vitae dignissim eu, iaculis sed purus. Vivamus faucibus, ipsum nec aliquet viverra, leo mauris condimentum ligula, sit amet sagittis enim ligula quis arcu. Nam egestas tortor id nisi porttitor mattis. In tortor ante, ultricies in suscipit a, tempus non massa. Vivamus et auctor mi. Fusce vel massa nulla. Phasellus nec eros mauris, et scelerisque orci. Donec malesuada orci vitae nulla accumsan porta a id massa. Quisque accumsan iaculis magna sit amet fringilla. Maecenas consequat, magna eget tincidunt semper, odio nibh rutrum mi, id feugiat ante nisi eu risus. Vestibulum nunc orci, rhoncus a placerat in, ultricies in mi. Cras mattis varius eros, vel fringilla nisi suscipit eget.</p>
      <p>Quisque scelerisque sagittis nulla at porttitor. Mauris a justo et tellus interdum tristique. Sed id augue vitae urna euismod commodo aliquet a quam. Pellentesque arcu velit, cursus et malesuada ut, consequat et diam. Nullam erat sem, rhoncus id ullamcorper vitae, rhoncus et arcu. In ultricies ultricies nulla, ut rutrum nisi iaculis at. Donec eu magna a metus ornare faucibus. Fusce aliquet faucibus ultricies. Morbi semper, est id tincidunt gravida, sem arcu adipiscing lacus, ac bibendum nulla leo eu purus. Quisque nec diam sed risus consectetur accumsan quis quis nibh. Vestibulum id purus lorem.</p>
    </section>

    <div class="sign-off">
      <div class="signature" role="img" aria-label="Handwritten signature"></div>
      <div class="signer-name">Martin Hale</div>
      <div class="signer-title">Co-Founder &amp; CEO</div>
    </div>

    <footer class="contact-footer">
      <div class="line">482 S. Harrow Avenue, Suite 310 Bellingham, WA 98417</div>
      <div class="line">
        <svg viewBox="0 0 24 24" aria-hidden="true"><path fill="#1f1f1f" d="M6.6 10.8a15 15 0 0 0 6.6 6.6l2.2-2.2c.3-.3.7-.4 1-.2 1.1.4 2.3.6 3.6.6.6 0 1 .4 1 1V20c0 .6-.4 1-1 1A17 17 0 0 1 3 4c0-.6.4-1 1-1h3.5c.6 0 1 .4 1 1 0 1.3.2 2.5.6 3.6.1.3 0 .7-.2 1z"/></svg>
        <span>360-555-2917</span>
        <svg viewBox="0 0 24 24" aria-hidden="true"><path fill="#1f1f1f" d="M7 3h10v5H7zM4 9h16a1 1 0 0 1 1 1v7h-4v4H7v-4H3v-7a1 1 0 0 1 1-1zm5 7v3h6v-3z"/></svg>
        <span>360-555-4068</span>
        <svg viewBox="0 0 24 24" aria-hidden="true"><circle cx="12" cy="12" r="9" fill="none" stroke="#1f1f1f" stroke-width="2"/><path d="M3 12h18M12 3c3 3 3 15 0 18M12 3c-3 3-3 15 0 18" fill="none" stroke="#1f1f1f" stroke-width="1.6"/></svg>
        <span>www.thornburycalder.example</span>
      </div>
    </footer>

    <div class="bottom-band"></div>
  </article>
</main>
</body>
</html>
```